Celling poster

It is a celling poster with questions that you ask yourself in the morning and a morning prayer + evening questions. People might put it on celling or on the wall.

Here is the contant, it is in Slovenian, but I have send you translation.

PO JUTRU SE DAN POZNA ...

1. Kaj me trenutno najbolj veseli v življenju?
3. Na kaj sem ponosna v življenju?
4. Za katere stvari danes čutim največ hvaležnosti?
5. V čem trenutno najbolj uživam?
6. Koga imam rada in kdo me ima rad?

Danes vstajam
s pomočjo nebeških sil:
svetlobe sonca,
sija lune,
žara ognja,
hitrosti strele,
okretnosti vetra,
globine morja,
stanovitnosti zemlje,
trdnosti skale.

VEČERNE MODROSTI

1. Kaj je bil danes moj prispevek svetu?
2. Kaj sem se danes naučila?
3. Katera situacija v dnevu mi je prinesla največ občutkov topline?

TRANSLATION for your understanding.

MORNING POWER QUESTIONS
1. What am I happy abou in my life right now?
2. What am I excited about in my life now?
3. What am I proud about in my life now?
4. What am I grateful about in my life now?
5. What am I enjoying most in my life now?
6. Who do I love? Who loves me?

MORNING PRAYER
Today I am waking up with the power of heavenly forces.
With the light of sun,
light of moon,
light of fire,
speed of lightning,
flexibility of wind,
depps of ocean,
stability of earth and
hardness of rock.

EVENING QUESTIONS OF WISDOM
1. What have I given today?
2. What did I learn today?
3. Which situations today gave me the most feelings of love, warmth?

```html
<!DOCTYPE html>
<html lang="sl">
<head>
<meta charset="utf-8">
<title>Po Jutru Se Dan Pozna – poster</title>
<link href="https://fonts.googleapis.com/css2?family=Kaushan+Script&display=swap" rel="stylesheet">
<style>
  :root {
    --page-bg: #ffffff;
    --paper-top: #fffdf0;
    --paper-mid: #fbf3cf;
    --paper-warm: #f6e6b4;
    --ink: #141210;
    --glow: #fff3b0;
    --lace: #8a7458;
    --lace-light: #c9b493;
    --mandala: #b59a76;
    --mandala-light: #efe4cf;
    --photo-haze: #d8cfc4;
    --photo-tree: #8e7a72;
    --photo-sun: #ffb43a;
    --photo-glow: #f07a1c;
  }
  html, body {
    margin: 0;
    width: 1200px;
    height: 649px;
    overflow: hidden;
    background: var(--page-bg);
  }
  .canvas {
    position: relative;
    width: 1200px;
    height: 649px;
  }
  .poster {
    position: absolute;
    left: 380px;
    top: 28px;
    width: 440px;
    height: 592px;
    overflow: hidden;
    background: linear-gradient(180deg, var(--paper-top) 0%, var(--paper-mid) 45%, var(--paper-warm) 70%);
    font-family: "Kaushan Script", cursive;
    color: var(--ink);
  }
  .photo-sunrise {
    position: absolute;
    left: 0; right: 0; bottom: 0;
    height: 290px;
    background:
      radial-gradient(circle at 48% 92%, var(--photo-sun) 0, var(--photo-glow) 9%, rgba(240,122,28,0.35) 24%, transparent 45%),
      linear-gradient(180deg, rgba(216,207,196,0) 0%, rgba(216,207,196,0.55) 30%, rgba(142,122,114,0.55) 70%, rgba(120,80,60,0.75) 100%);
  }
  .lace-border {
    position: absolute;
    left: 0; top: 0; bottom: 0;
    width: 18px;
    background: repeating-linear-gradient(180deg, var(--lace) 0 6px, var(--lace-light) 6px 12px);
    opacity: 0.85;
  }
  .mandala-top {
    position: absolute;
    left: 18px; right: 0; top: 0;
    height: 56px;
    background:
      radial-gradient(circle at 14% 0, var(--mandala-light) 0, var(--mandala) 55%, transparent 57%) 0 0 / 88px 56px repeat-x;
  }
  .mandala-right {
    position: absolute;
    right: 0; top: 40px; bottom: 0;
    width: 74px;
    background:
      radial-gradient(circle at 100% 50%, var(--mandala-light) 0, var(--mandala) 55%, transparent 57%) 0 0 / 74px 108px repeat-y;
  }
  .content {
    position: absolute;
    left: 26px;
    top: 0;
    right: 0;
    white-space: nowrap;
    text-shadow: 0 0 4px var(--glow), 0 0 2px var(--glow);
  }
  .heading {
    position: absolute;
    left: 0;
    margin: 0;
    font-weight: 400;
    font-size: 21px;
    line-height: 1;
  }
  .question-list, .prayer {
    position: absolute;
    left: 0;
    margin: 0;
    padding: 0;
    list-style: none;
  }
  .question-list li {
    font-size: 13px;
    line-height: 1;
    height: 22px;
  }
  .morning-title { top: 58px; }
  .morning-questions { top: 103px; }
  .prayer-title { top: 216px; font-size: 19px; }
  .prayer { top: 241px; font-size: 11.5px; line-height: 16.5px; }
  .evening-title { top: 408px; font-size: 19px; }
  .evening-questions { top: 451px; }
  .evening-questions li { height: 23px; }
</style>
</head>
<body>
<div class="canvas">
  <article class="poster">
    <div class="photo-sunrise" role="img" aria-label="Photo of bare trees silhouetted against a rising sun"></div>
    <div class="lace-border" role="img" aria-label="Brown lace ornament border"></div>
    <div class="mandala-top" role="img" aria-label="Row of brown mandala ornaments"></div>
    <div class="mandala-right" role="img" aria-label="Column of brown mandala ornaments"></div>

    <div class="content">
      <h1 class="heading morning-title">Po Jutru Se Dan Pozna</h1>
      <ol class="question-list morning-questions">
        <li>1. Kaj me trenutno najbolj veseli v življenju?</li>
        <li>3. Na kaj sem ponosna v življenju?</li>
        <li>4. Za katere stvari danes čutim največ hvaležnosti?</li>
        <li>5. V čem trenutno najbolj uživam?</li>
        <li>6. Koga imam rada in kdo me ima rad?</li>
      </ol>

      <h2 class="heading prayer-title">Danes vstajam</h2>
      <p class="prayer">
        s pomočjo nebeških sil:<br>
        svetlobe sonca,<br>
        sija lune,<br>
        žara ognja,<br>
        hitrosti strele,<br>
        okretnosti vetra,<br>
        globine morja,<br>
        stanovitnosti zemlje,<br>
        trdnosti skale.
      </p>

      <h2 class="heading evening-title">Večerne Modrosti</h2>
      <ol class="question-list evening-questions">
        <li>1. Kaj je bil danes moj prispevek svetu?</li>
        <li>2. Kaj sem se danes naučila?</li>
        <li>3. Katera situacija v dnevu mi je prinesla največ občutkov topline?</li>
      </ol>
    </div>
  </article>
</div>
</body>
</html>
```